Copperleaf Dukes - Sovereign rings, pendants & custom cultural pieces

I need a website that attracts customers knowing that I am as per detailed below Everyone deserves a special piece of treasure. At Copperleaf Dukes we provide you with unique, high-quality and affordable Sovereign rings, pendants & custom cultural pieces.
Feel free to check my Snapgallery page to get idea's @copperleaf.dukes
I want people to see the Items I have available & know that my prices are very competitive. I want people to be able to Shop/Purchase items via site. I would like to have Copperleaf Dukes Chatterbook, Snapgallery & Swapyard Icon/tabs on site so customers can link a at click of the mouse.

(My Apologies to you all, This is all overwhelming & new to myself & I appreciate your efforts & work detail)
Updates

Apologies, have had family loss to deal with

Still dealing with loss of family member

Still Dealing with Family member passing

As previously, still getting through the loss of a family member

As per previous extensions, re adjusting to life after loss of family member

As per previously still recovering from loss of family member

As previously expressed

Haven’t recovered from family loss

I am still getting life back together

Target Market(s)

Jewellery, Wedding, Gifts, Pacific people, Persons 18 - 65yrs, New Zealand & Australian

Industry/Entity Type

Jewelry

Contact Information for Business Card

Copperleaf Dukes
Rek Tamuno
Chatterbook @copperleafdukes
Snapgallery @copperleaf.dukes
Phone Number 021 04731952
Website www.copperleafdukes.co.nz
Auckland
New Zealand

Number of Pages Required

5+ page

Font styles to use
Sans Serif

Colors
474747
1b1b1b
000000
cfcfcf
fbed22
ffc214
ffffff

Requirements
Must have
• Using Black / Gold Copperleaf Dukes logo with crown, has been attached to Web design.
• Rek Tamuno
• Chatterbook Copperleaf Dukes
• Snapgallery @copperleaf.dukes
• Swapyard Copperleaf Dukes
• Phone Number 021 04731952
• Website www.copperleafdukes.co.nz
Nice to have
• Thinking black card with the Copperleaf Dukes Gold logo
• Lines on back of card for Customer Quoted Prices

```html
<!DOCTYPE html>
<html lang="en">
<head>
<meta charset="utf-8">
<title>Copperleaf Dukes – Business Card</title>
<link rel="stylesheet" href="https://fonts.googleapis.com/css2?family=Poppins:wght@400;500;700&display=swap">
<style>
  :root {
    --backdrop: #e6e2dc;
    --card-black: #000000;
    --card-white: #ffffff;
    --gold: #7d6a1c;
    --text-dark: #1b1b1b;
    --icon-gold: #8a7424;
  }
  * { margin: 0; padding: 0; box-sizing: border-box; }
  html, body { width: 1200px; height: 685px; overflow: hidden; }
  body {
    background: var(--backdrop);
    font-family: "Poppins", sans-serif;
    position: relative;
  }
  .card {
    position: absolute;
    top: 188px;
    width: 540px;
    height: 310px;
    overflow: hidden;
    box-shadow: 0 6px 18px rgba(0,0,0,0.25);
  }
  .card--front { left: 40px; background: var(--card-black); }
  .card--back { left: 620px; background: var(--card-white); }
  .card svg.card__shapes { position: absolute; inset: 0; }

  .brand-name {
    position: absolute;
    font-family: "Poppins", sans-serif;
    font-weight: 500;
    color: var(--gold);
    white-space: nowrap;
    letter-spacing: 0.5px;
  }
  .card--front .brand-name {
    left: 0; right: 0; top: 140px;
    text-align: center;
    font-size: 24px;
  }
  .card--back .brand-name {
    left: 28px; top: 118px;
    font-size: 15px;
  }

  .contact {
    position: absolute;
    right: 26px;
    top: 42px;
    text-align: right;
  }
  .contact__name {
    font-weight: 700;
    font-size: 24px;
    letter-spacing: 1px;
    color: var(--text-dark);
    margin-bottom: 14px;
  }
  .contact__list { list-style: none; }
  .contact__item {
    display: flex;
    justify-content: flex-end;
    align-items: center;
    gap: 10px;
    font-size: 15px;
    color: var(--text-dark);
    height: 33px;
  }
  .contact__icon { width: 18px; height: 18px; flex: none; }
</style>
</head>
<body>

  <section class="card card--front" aria-label="Card front">
    <svg class="card__shapes" width="540" height="310" viewBox="0 0 540 310" aria-hidden="true">
      <rect x="62" y="0" width="8" height="150" fill="#ffffff"/>
      <rect x="80" y="0" width="8" height="182" fill="var(--gold)"/>
      <rect x="452" y="142" width="8" height="168" fill="var(--gold)"/>
      <rect x="470" y="200" width="8" height="110" fill="#ffffff"/>
    </svg>
    <div class="brand-name">Copperleaf Dukes</div>
  </section>

  <section class="card card--back" aria-label="Card back">
    <svg class="card__shapes" width="540" height="310" viewBox="0 0 540 310" aria-hidden="true">
      <polygon points="0,0 350,0 30,310 0,310" fill="var(--card-black)"/>
      <polygon points="350,0 370,0 50,310 30,310" fill="var(--gold)"/>
    </svg>
    <div class="brand-name">Copperleaf Dukes</div>

    <div class="contact">
      <div class="contact__name">REK TAMUNO</div>
      <ul class="contact__list">
        <li class="contact__item">021 04731952
          <svg class="contact__icon" viewBox="0 0 18 18" aria-hidden="true"><path d="M4 2l3 3-1.6 2a9 9 0 0 0 5.6 5.6L13 11l3 3-2 2C7 15 3 11 2 4z" fill="none" stroke="var(--icon-gold)" stroke-width="1.4"/></svg>
        </li>
        <li class="contact__item">www.copperleafdukes.co.nz
          <svg class="contact__icon" viewBox="0 0 18 18" aria-hidden="true"><g fill="none" stroke="var(--icon-gold)" stroke-width="1.3"><circle cx="9" cy="9" r="7"/><ellipse cx="9" cy="9" rx="3" ry="7"/><line x1="2" y1="9" x2="16" y2="9"/></g></svg>
        </li>
        <li class="contact__item">Copperleaf Dukes
          <svg class="contact__icon" viewBox="0 0 18 18" aria-hidden="true"><rect x="1" y="1" width="16" height="16" rx="2" fill="var(--icon-gold)"/></svg>
        </li>
        <li class="contact__item">@copperleaf.dukes
          <svg class="contact__icon" viewBox="0 0 18 18" aria-hidden="true"><rect x="1" y="1" width="16" height="16" rx="2" fill="var(--icon-gold)"/></svg>
        </li>
        <li class="contact__item">Copperleaf_dukes
          <svg class="contact__icon" viewBox="0 0 18 18" aria-hidden="true"><rect x="1" y="1" width="16" height="16" rx="2" fill="var(--icon-gold)"/></svg>
        </li>
      </ul>
    </div>
  </section>

</body>
</html>
```